Teilnehmerzertifikat für Expeditionsmobil
Zielgruppe
Wir bitten alles Rund um das Thema Expeditionsmobil an. Unter anderem unsere Lagerfeuer und Weite Fahrt nach Tunesien und dafür benötige ich ein Teilnehmer Zertifikat.
Aufgabenstellung
Im Hintergrund soll ein Bild von der Sahara verarbeitet sein und im Vordergrund möchte ich von jedem Teilnehmer ein Bild mit dem eigenen Expeditonsfahrzeug einfügen. Das Zertifikat soll persöhnlich und wie von einem Freund sein

```html
<!DOCTYPE html>
<html lang="de">
<head>
<meta charset="UTF-8">
<title>Teilnehmer-Zertifikat – Lagerfeuer und Weite Fahrt</title>
<link href="https://fonts.googleapis.com/css2?family=Rubik+Distressed&family=Lexend:wght@300;400;700&family=Montserrat:wght@800&family=Mr+Dafoe&display=swap" rel="stylesheet">
<style>
  :root {
    --page-bg: #e6e6e8;
    --ink-black: #0b0b0b;
    --brand-red: #e8272c;
    --paper-white: #ffffff;
    --sky-top: #8fb8d8;
    --sky-low: #c9dbe6;
    --sand-light: #d3a878;
    --sand-dark: #9c7150;
  }
  * { margin: 0; padding: 0; box-sizing: border-box; }
  html, body {
    width: 1200px; height: 800px; overflow: hidden;
    background: var(--page-bg);
  }
  .certificate {
    position: absolute; left: 50px; top: 20px;
    width: 1100px; height: 760px;
    overflow: hidden;
    background: var(--ink-black);
    font-family: "Lexend", sans-serif;
    color: var(--paper-white);
  }
  .certificate-shapes { position: absolute; inset: 0; }
  .certificate-title {
    position: absolute; left: 50px; top: 56px;
    font-family: "Rubik Distressed", system-ui, sans-serif;
    font-size: 50px; line-height: 1.02; letter-spacing: 1px;
    text-transform: uppercase;
  }
  .awarded-to {
    position: absolute; left: 200px; top: 178px;
    font-weight: 300; font-size: 28px;
  }
  .recipient-name {
    position: absolute; left: 160px; top: 262px;
    font-family: "Montserrat", sans-serif; font-weight: 800;
    font-size: 40px; letter-spacing: 1px; line-height: 1;
  }
  .recipient-name span { display: table; padding: 12px 22px 10px; }
  .recipient-name .first-name { background: var(--brand-red); }
  .recipient-name .last-name { background: var(--ink-black); margin-left: 28px; }
  .vehicle-photo {
    position: absolute; left: 540px; top: 78px;
    width: 400px; height: 300px;
    background: var(--paper-white); padding: 10px;
    box-shadow: 0 4px 14px rgba(0,0,0,.35);
  }
  .vehicle-photo div {
    width: 100%; height: 100%;
    background: linear-gradient(180deg, #7d7f8c 0%, #b98457 30%, #a86e4a 60%, #8f6a58 100%);
  }
  .certificate-message {
    position: absolute; left: 64px; top: 462px; width: 680px;
    font-size: 17px; line-height: 1.3;
  }
  .certificate-message p + p { margin-top: 10px; }
  .signature-line {
    position: absolute; left: 220px; top: 600px;
    display: flex; align-items: baseline; gap: 16px;
  }
  .signature-line .place-date { font-size: 17px; }
  .signature-line .signature {
    font-family: "Mr Dafoe", cursive; font-size: 52px; line-height: 1;
  }
  .tour-name {
    position: absolute; left: 800px; top: 420px; width: 250px;
    font-weight: 700; font-size: 38px; line-height: 1.05;
    text-transform: uppercase; text-align: center;
  }
  .organizer {
    position: absolute; right: 44px; bottom: 40px;
    display: flex; align-items: center; gap: 12px;
    color: var(--brand-red);
    font-weight: 700; font-size: 28px; line-height: 1; text-transform: uppercase;
  }
  .organizer i {
    width: 34px; height: 34px; border-radius: 50%;
    background: var(--brand-red); display: block; flex: none;
  }
</style>
</head>
<body>
<main class="certificate">
  <svg class="certificate-shapes" width="1100" height="760" viewBox="0 0 1100 760">
    <defs>
      <linearGradient id="sahara-tones" x1="0" y1="0" x2="0" y2="1">
        <stop offset="0" stop-color="var(--sky-top)"/>
        <stop offset="0.22" stop-color="var(--sky-low)"/>
        <stop offset="0.4" stop-color="var(--sand-light)"/>
        <stop offset="1" stop-color="var(--sand-dark)"/>
      </linearGradient>
    </defs>
    <rect class="sahara-backdrop" x="0" y="0" width="1100" height="520" fill="url(#sahara-tones)" role="img" aria-label="Foto der Sahara mit Wüstenpiste und Fahrzeugkolonne"/>
    <path class="title-brush" fill="var(--ink-black)"
      d="M0 0 H470 L455 20 L478 40 L450 62 L470 84 L445 110 L462 135 L430 160 L448 185 L410 200 L380 206 L300 210 L180 222 L60 240 L0 252 Z"/>
    <path class="message-band" fill="var(--brand-red)"
      d="M0 410 L240 380 L560 360 L800 330 L1100 310 V600 L1060 606 L1020 600 L980 612 L900 620 L860 628 L780 646 L700 660 L640 668 L560 684 L480 694 L400 702 L300 712 L200 720 L120 726 L0 736 Z"/>
    <path class="footer-band" fill="var(--ink-black)"
      d="M0 736 L120 726 L200 720 L300 712 L400 702 L480 694 L560 684 L640 668 L700 660 L780 646 L860 628 L900 620 L980 612 L1020 600 L1060 606 L1100 600 V760 H0 Z"/>
  </svg>

  <h1 class="certificate-title">Teilnehmer-<br>Zertifikat</h1>
  <p class="awarded-to">verliehen an:</p>

  <h2 class="recipient-name">
    <span class="first-name">MAXIMILLIAN</span>
    <span class="last-name">MUSTERMANN</span>
  </h2>

  <figure class="vehicle-photo">
    <div role="img" aria-label="Foto des Teilnehmers mit seinem roten Expeditionsmobil bei einer Wasserdurchfahrt in der Wüste"></div>
  </figure>

  <section class="certificate-message">
    <p>Ihr habt mit Begeisterung und Abenteuerlust an unserer gemeinsamen Reise durch Tunesien teilgenommen.</p>
    <p>Mit eurem Expeditionsmobil habt ihr die Wüste bezwungen, neue Freundschaften geschlossen und die Magie dieses einzigartigen Landes erlebt.</p>
    <p>Danke, dass ihr Teil dieser besonderen Tour wart – auf viele weitere Abenteuer!</p>
  </section>

  <div class="signature-line">
    <span class="place-date">Tunisien, 21 November 2024</span>
    <span class="signature">Jens &amp; Malte</span>
  </div>

  <p class="tour-name">Lagerfeuer und Weite Fahrt</p>

  <div class="organizer"><i></i>Kranichpfad Reisen</div>
</main>
</body>
</html>
```